Manufacturers Catalog Cover Page

We are looking to have a cover to our catalog page designed. I currently have begun work for the remained of the catalog in InDesign and want the cover created in InDesign. I will provide photos.

Looking to beable to add the cover to our existing attached catalog.

Industry/Entity Type

Manufacturing

Requirements
Must have
• Colors match what we are currently using. The Dark grey and gold
Nice to have
• modern, clean

```html
<!DOCTYPE html>
<html lang="en">
<head>
<meta charset="utf-8">
<title>Paragon Polymers Catalog Cover</title>
<link href="https://fonts.googleapis.com/css2?family=Oswald:wght@400;500;600&display=swap" rel="stylesheet">
<style>
  :root{
    --stage:#a9a9a9;
    --charcoal:#2f2e2d;
    --gold:#c8b284;
    --gold-text:#d2bd8c;
    --white:#ffffff;
  }
  *{margin:0;padding:0;box-sizing:border-box}
  html,body{width:1200px;height:790px;overflow:hidden;background:var(--stage)}
  body{font-family:"Oswald",sans-serif;position:relative}
  .spread{position:absolute;left:60px;top:35px;width:1080px;height:720px;display:flex;box-shadow:0 10px 30px rgba(0,0,0,.3)}
  .panel{position:relative;width:540px;height:720px;background:var(--charcoal);overflow:hidden}
  .panel--back{border-right:1px solid #3c3b3a}
  .tile{position:absolute;width:128px;height:128px}
  .tile--gold{background:var(--gold)}
  .kicker{position:absolute;color:var(--white);font-weight:500;font-size:21px;line-height:1.15;text-transform:uppercase;letter-spacing:.2px}
  .rule{position:absolute;width:44px;height:1px;background:var(--gold)}
  .headline{position:absolute;color:var(--gold-text);font-weight:500;font-size:33px;line-height:1.12;text-transform:uppercase}
  .brand{position:absolute;display:flex;align-items:center;gap:14px}
  .brand__dot{width:60px;height:60px;border-radius:50%;background:var(--gold)}
  .brand__name{color:var(--white);font-weight:500;font-size:21px;line-height:1.15;text-transform:uppercase}
  .phones{position:absolute;color:var(--white);font-weight:500;font-size:29px;line-height:1.05}
  .web{position:absolute;color:var(--gold-text);font-weight:500;font-size:15px;letter-spacing:.6px;text-transform:uppercase}
  .band{position:absolute;left:0;top:620px;width:540px;height:72px;background:var(--gold)}
  .band .web{right:30px;bottom:14px;color:var(--charcoal);font-size:16px}
</style>
</head>
<body>
<main class="spread">
  <section class="panel panel--back">
    <p class="kicker" style="left:50px;top:150px">Rubber &amp;<br>Plastic Extursion</p>
    <div class="rule" style="left:50px;top:210px"></div>
    <h2 class="headline" style="left:50px;top:222px">Gaskets,<br>Trims &amp; Seals</h2>

    <div class="tile tile--gold" style="left:413px;top:110px"></div>
    <div class="tile" role="img" aria-label="Coiled white and brown extruded rubber profiles" style="left:276px;top:247px;background:linear-gradient(135deg,#f3f1ef,#c9a394)"></div>
    <div class="tile" role="img" aria-label="Red, black and tan trim seal coils" style="left:413px;top:247px;background:linear-gradient(135deg,#f2eeea,#b44a3c 55%,#8b7458)"></div>
    <div class="tile" role="img" aria-label="Yellow backhoe loader under blue sky" style="left:413px;top:384px;background:linear-gradient(180deg,#6d9ccf,#b8c9d8 55%,#b08a4a)"></div>
    <div class="tile tile--gold" style="left:413px;top:521px;height:140px"></div>

    <div class="brand" style="left:50px;top:525px">
      <div class="brand__dot"></div>
      <p class="brand__name">Paragon<br>Polymers</p>
    </div>
    <p class="phones" style="left:50px;top:610px">888-555-0142<br>330-555-0187</p>
    <p class="web" style="left:50px;top:682px">www.paragonpolymers.com</p>
  </section>

  <section class="panel panel--front">
    <div class="brand" style="left:50px;top:40px">
      <div class="brand__dot"></div>
      <p class="brand__name">Paragon<br>Polymers</p>
    </div>
    <p class="kicker" style="left:50px;top:135px">Rubber &amp;<br>Plastic Extursion</p>
    <div class="rule" style="left:50px;top:195px"></div>
    <h1 class="headline" style="left:50px;top:207px">Gaskets,<br>Trims &amp; Seals</h1>

    <div class="tile" role="img" aria-label="Motorhome on a desert road" style="left:411px;top:70px;background:linear-gradient(180deg,#8fb3d6,#a77a58 50%,#5b4a3d)"></div>
    <div class="tile" role="img" aria-label="Black extruded rubber seal coils" style="left:274px;top:207px;background:linear-gradient(135deg,#f1f1f1,#3a3a3c 60%,#dcdcdc)"></div>
    <div class="tile" role="img" aria-label="Yellow industrial robots on an assembly line" style="left:411px;top:207px;background:linear-gradient(135deg,#a9c4dc,#d8b23a 50%,#6f8aa3)"></div>
    <div class="tile tile--gold" style="left:137px;top:344px"></div>
    <div class="tile" role="img" aria-label="Refinery stacks reflected in water" style="left:274px;top:344px;background:linear-gradient(180deg,#7fa9d6,#c7d4dc 50%,#6b84a0)"></div>
    <div class="tile tile--gold" style="left:411px;top:344px"></div>
    <div class="tile" role="img" aria-label="Speedboat on open sea" style="left:0;top:481px;background:linear-gradient(160deg,#4f8fc0,#1f5b86 60%,#dfe8ee)"></div>
    <div class="tile" role="img" aria-label="Yellow combine harvester in a field" style="left:137px;top:481px;background:linear-gradient(180deg,#8fb6dc,#d9b53b 55%,#b09264)"></div>
    <div class="tile" role="img" aria-label="Modern glass office building" style="left:274px;top:481px;background:linear-gradient(135deg,#b9cde0,#e6ebee 50%,#6f9a6a)"></div>
    <div class="tile" role="img" aria-label="Silver car driving at sunset" style="left:411px;top:481px;background:linear-gradient(160deg,#6a9ed0,#c4c8cc 50%,#b7894a)"></div>

    <div class="band"><p class="web">www.paragonpolymers.com</p></div>
  </section>
</main>
</body>
</html>
```